VeloShield broucher for business to business marketing

I will attach a broucher if a supplier company I need this to be rebranded under my company name with a different look and appeal. The colour code I need is light blue and dark navyblue. Refer website for colour (www.veloshield-example.co.uk). All the information remains sane but slight different wording will be appreciated.

Refer website: www.prabelix-example.com or Kreva for referrence

Target Market(s)

We are an antimicrobial coating company who aim to provide service in Central London and Westminster area covering, Schools
Corporate office
Playgrounds
Communal space
Gym
Private clinics
Dentist
Retail shops
Offices and private residential homes

Font styles to use
Serif

Colors
0355a3
eaf1f7
cfdfed
35a7d7
85cae6
ffffff
85acd3

Requirements
Must have
• All the information available in the leaflet (Tallow Vex one) but with branding of (VeloShield) instead of TallowVex. In small print can write at below or somewhere that we are partner of Tallow Vex or in partnership of Tallowvex

Must have product details and it's explanations
Must have display sticker details
Must have areas coved or services with pictures
Nice to have
• Nice to have some change in display sticker design (this area is antimicrobial protected one)
Nice to have pictures for all industries covered
Nice to have different graphic representation of the spike photo in product info
Should not have
• Exactly same words like Tallow Vex and exact same photos no please

```html
<!DOCTYPE html>
<html lang="en">
<head>
<meta charset="utf-8">
<title>VeloShield Flyer</title>
<link rel="stylesheet" href="https://fonts.googleapis.com/css2?family=PT+Serif:wght@400;700&display=swap">
<style>
  :root {
    --navy: #0355a3;
    --navy-deep: #0b4f9e;
    --mid-blue: #2d70b8;
    --sky: #35a7d7;
    --ice: #eaf1f7;
    --white: #ffffff;
    --ink: #1a1a1a;
    --photo-light: #dedbd8;
    --photo-dark: #bdb8b3;
    --gold-light: #f6d66a;
    --gold-dark: #b7861c;
    --page: #e9ecef;
  }
  * { margin: 0; padding: 0; box-sizing: border-box; }
  html, body {
    width: 1200px; height: 800px; overflow: hidden;
    background: var(--page);
  }
  .canvas { position: relative; width: 1200px; height: 800px; }
  .flyer {
    position: absolute; left: 330px; top: 18px;
    width: 710px; height: 1005px;
    transform: scale(0.7606); transform-origin: top left;
    overflow: hidden;
    box-shadow: 0 12px 40px rgba(3, 40, 90, 0.18);
    font-family: "PT Serif", serif;
  }
  .flyer-shapes { position: absolute; inset: 0; }
  .brand {
    position: absolute; left: 17px; top: 20px; width: 168px;
    text-align: center; color: var(--white);
  }
  .brand-mark {
    width: 44px; height: 44px; margin: 0 auto 18px;
    background: rgba(255, 255, 255, 0.85);
  }
  .brand-name { font-weight: 700; font-size: 26px; line-height: 1; }
  .brand-tagline { font-size: 11px; margin-top: 4px; }
  .headline {
    position: absolute; left: 38px; top: 508px;
    font-weight: 700; font-size: 54px; line-height: 1.1;
    color: var(--white);
  }
  .intro {
    position: absolute; left: 55px; top: 608px;
    font-size: 13.5px; line-height: 18.3px; color: var(--white);
  }
  .sectors {
    position: absolute; left: 33px; top: 806px;
    font-size: 11.5px; line-height: 15.5px; color: var(--ink);
  }
  .sticker-callout {
    position: absolute; right: 16px; top: 834px;
    font-size: 14px; line-height: 19px; color: var(--white); text-align: right;
  }
  .sticker-details {
    position: absolute; left: 386px; top: 909px;
    font-size: 10.5px; line-height: 15px; color: var(--white);
  }
</style>
</head>
<body>
<div class="canvas">
  <article class="flyer">
    <svg class="flyer-shapes" viewBox="0 0 710 1005" width="710" height="1005">
      <defs>
        <linearGradient id="bg-blue" x1="0" y1="0" x2="0" y2="1">
          <stop offset="0" stop-color="var(--mid-blue)"/>
          <stop offset="1" stop-color="var(--navy)"/>
        </linearGradient>
        <linearGradient id="photo-tone" x1="0" y1="0" x2="1" y2="1">
          <stop offset="0" stop-color="var(--photo-light)"/>
          <stop offset="1" stop-color="var(--photo-dark)"/>
        </linearGradient>
        <linearGradient id="foot-tone" x1="0" y1="0" x2="1" y2="0">
          <stop offset="0" stop-color="var(--white)"/>
          <stop offset="1" stop-color="var(--ice)"/>
        </linearGradient>
        <radialGradient id="seal-tone" cx="0.4" cy="0.35" r="0.7">
          <stop offset="0" stop-color="var(--gold-light)"/>
          <stop offset="1" stop-color="var(--gold-dark)"/>
        </radialGradient>
      </defs>
      <rect class="base" width="710" height="1005" fill="url(#bg-blue)"/>
      <path class="diagonal-band" d="M0,160 L330,0 H420 L0,420 Z" fill="var(--navy-deep)" opacity="0.25"/>
      <path class="hero-photo" role="img" aria-label="Photo: hand pressing the pump of a hand sanitiser dispenser"
            d="M370,0 H710 V478 L565,595 Q515,635 470,590 L185,265 Q148,220 190,180 Z" fill="url(#photo-tone)"/>
      <path class="sky-wedge" d="M0,337 L390,762 H0 Z" fill="var(--sky)"/>
      <path class="footer-panel" d="M0,762 H395 Q440,762 472,736 L710,550 V1005 H0 Z" fill="url(#foot-tone)"/>
      <path class="navy-corner" d="M340,1005 V900 Q340,830 410,790 L710,572 V1005 Z" fill="var(--navy)"/>
      <circle class="guarantee-seal" role="img" aria-label="Satisfaction guarantee seal" cx="98" cy="925" r="52" fill="url(#seal-tone)"/>
    </svg>

    <header class="brand">
      <div class="brand-mark"></div>
      <div class="brand-name">VeloShield</div>
      <div class="brand-tagline">Your smart antimicrobial shield</div>
    </header>

    <h1 class="headline">VeloShield</h1>

    <p class="intro">
      An invisible antimicrobial coating for everyday surfaces.<br>
      It bonds to hard and soft materials and keeps working<br>
      long after cleaning, reducing bacteria and viruses.<br>
      Non-toxic and alcohol-free, safe around children.<br>
      Applied by trained technicians across Central London.
    </p>

    <p class="sectors">
      Serving schools, offices, gyms, clinics, dentists, retail,<br>
      playgrounds, communal spaces and private homes.
    </p>

    <p class="sticker-callout">
      Look for the VeloShield sticker:<br>
      this area is antimicrobial protected.
    </p>

    <p class="sticker-details">
      Every treated site receives a clear display sticker<br>
      showing the date applied and the next service due,<br>
      so staff and visitors can see the protection in place.<br>
      Central London &amp; Westminster · www.veloshield-example.co.uk<br>
      In partnership with Tallow Vex antimicrobial technology.
    </p>
  </article>
</div>
</body>
</html>
```